Brivane - Business Cards for a new venture

create business card for a startup classified business dealing in construction materials, the cards need to have a professional look but modern, more serious than playful, one of the samples must include the official font (attached), please explore using the official colors in the company's logo

Target Market(s)

Energy sector

Contact Information for Business Card

Font styles to use
Other font styles liked:
• suissnord

Requirements
Must have
• corporate colors (in logo attached)
Nice to have
• Official font (in one of the samples) font is : suissnord
Should not have
• Cartoonish look

```html
<!DOCTYPE html>
<html lang="en">
<head>
<meta charset="utf-8">
<title>Brivane Business Cards</title>
<link href="https://fonts.googleapis.com/css2?family=Roboto:wght@300;400&family=Roboto+Condensed:wght@400;700&display=swap" rel="stylesheet">
<style>
  :root {
    --navy: #0d4370;
    --paper: #f3f3f3;
    --steel: #9a9a9c;
    --wordmark: #8c8c8e;
    --white: #ffffff;
    --backdrop: #e4e2df;
  }
  * { margin: 0; padding: 0; box-sizing: border-box; }
  html, body {
    width: 1200px; height: 960px; overflow: hidden;
    background: var(--backdrop);
  }
  .canvas { position: relative; width: 1200px; height: 960px; }

  .card {
    position: absolute; width: 600px; height: 343px;
    box-shadow: 0 3px 6px rgba(0,0,0,0.25);
    overflow: hidden;
  }
  .card-front { left: 314px; top: 113px; background: var(--paper); }
  .card-back { left: 312px; top: 472px; background: var(--navy); }

  .edge-bar {
    position: absolute; left: 0; top: 54px; width: 12px; height: 235px;
    background: var(--steel);
  }
  .front-wordmark {
    position: absolute; left: 36px; top: 196px; width: 222px;
    text-align: center;
    font-family: "Roboto", sans-serif; font-weight: 300;
    font-size: 24px; letter-spacing: 4px; color: var(--wordmark);
    text-transform: uppercase;
  }

  .contact-panel {
    position: absolute; left: 332px; top: 44px; width: 268px; height: 254px;
    background: var(--navy); color: var(--white);
    border-radius: 30px 0 0 30px;
    padding: 33px 0 0 41px;
  }
  .person-name {
    font-family: "Roboto Condensed", sans-serif; font-weight: 700;
    font-size: 21px; line-height: 24px;
  }
  .person-role {
    font-family: "Roboto Condensed", sans-serif; font-weight: 400;
    font-size: 16px; line-height: 20px; margin-top: 1px;
  }
  .address {
    font-family: "Roboto", sans-serif; font-size: 14.5px; line-height: 19px;
    margin-top: 20px; font-style: normal;
  }
  .contact-list { list-style: none; margin-top: 10px; }
  .contact-list li {
    font-family: "Roboto", sans-serif; font-size: 14.5px; line-height: 19.5px;
    display: flex; align-items: center;
  }
  .contact-list svg { width: 13px; height: 13px; margin-right: 9px; fill: var(--white); flex: none; }

  .back-wordmark {
    position: absolute; left: 0; top: 138px; width: 100%;
    text-align: center;
    font-family: "Roboto", sans-serif; font-weight: 400;
    font-size: 46px; letter-spacing: 10px; color: var(--white);
    text-transform: uppercase;
  }
  .back-url {
    position: absolute; left: 0; top: 289px; width: 100%;
    text-align: center;
    font-family: "Roboto", sans-serif; font-size: 15px;
    letter-spacing: 8.5px; color: var(--white);
  }
</style>
</head>
<body>
<main class="canvas">
  <section class="card card-front">
    <div class="edge-bar"></div>
    <div class="front-wordmark">Brivane</div>
    <div class="contact-panel">
      <div class="person-name">DANIEL REYES</div>
      <div class="person-role">CEO/FOUNDER</div>
      <address class="address">4120 Harbor View Road<br>Juneau, Alaska 34812</address>
      <ul class="contact-list">
        <li><svg viewBox="0 0 16 16" aria-hidden="true"><path d="M3.6 1l2.6 3-1.5 1.8c.9 2 2.4 3.5 4.4 4.4L10.9 8.7l3.1 2.6-1.4 2.9C6.7 14 2 9.3 1.7 3.4z"/></svg>512 804 1736</li>
        <li><svg viewBox="0 0 16 16" aria-hidden="true"><path d="M4.5 0h7a1 1 0 0 1 1 1v14a1 1 0 0 1-1 1h-7a1 1 0 0 1-1-1V1a1 1 0 0 1 1-1zm.8 2v10.5h5.4V2zM8 13.3a.9.9 0 1 0 0 1.8.9.9 0 0 0 0-1.8z"/></svg>728 315 9042</li>
        <li><svg viewBox="0 0 16 16" aria-hidden="true"><path d="M1 3.5h14v1L8 9 1 4.5zM1 6l7 4.5L15 6v6.5H1z"/></svg>daniel@brivane.com</li>
        <li><svg viewBox="0 0 16 16" aria-hidden="true"><path d="M8 1a7 7 0 1 0 0 14A7 7 0 0 0 8 1zm-1 2.2 1.5 1.6-1 1.6H5.3L4 5A5 5 0 0 1 7 3.2zm3.5 3.3 2.3.6a5 5 0 0 1-2.3 5.3l-.6-2.7-1.9-.7z"/></svg>www.brivane.com</li>
      </ul>
    </div>
  </section>

  <section class="card card-back">
    <div class="back-wordmark">Brivane</div>
    <div class="back-url">www.brivane.com</div>
  </section>
</main>
</body>
</html>
```